Twin Harbor Keystone Method

We are a wealth advisory firm. We need a design that shows our business is built on seven pillars. These seven pillars support all 85 things. These seven pillars form the foundation of our process. As their lives unfold and their needs evolve, they can’t outgrow our process; they’ll grow into it as critical life events occur and their lives progress.

We have an example of pillars, a figure of 8, and trees—we would like it to be modern, clean, and nature-inspired. If you use pillars, they cannot look 80s or like a law office. I am also attaching a picture of our logo and the landing page of our website for reference to our feel and style.
We want to use the language on the sheet with figure 8 in the final design.

Target Market(s)

families and small business owners with 1 million + of investable assets

Industry/Entity Type

Finance

Font styles to use
Sans Serif

Colors
0054AA
0677BA
7BADD7
CADEEF
E8F1F8
FFC000
F8CF3A
FAE287
FDF2CF
FEFAEE
EE7325
F08F49
F5BC92
FAE3D3
FDF4ED

```html
<!DOCTYPE html>
<html lang="en">
<head>
<meta charset="utf-8">
<title>Keystone Method – 85 Things</title>
<link rel="stylesheet" href="https://fonts.googleapis.com/css2?family=Montserrat:wght@600;700;800&family=Bebas+Neue&display=swap">
<style>
  :root {
    --page-bg: #b1b1b1;
    --card-bg: #ffffff;
    --navy: #213a86;
    --navy-light: #2a4a9c;
    --orange: #e0580f;
    --orange-ring: #f5a56b;
    --orange-glow: #fbd3b4;
    --label: #444444;
    --band: #4a4a4a;
    --white: #ffffff;
  }
  * { margin: 0; padding: 0; box-sizing: border-box; }
  html, body {
    width: 812px;
    height: 1200px;
    overflow: hidden;
    background: var(--page-bg);
  }
  .stage {
    width: 812px;
    height: 1200px;
    display: flex;
    align-items: center;
    justify-content: center;
  }
  .banner {
    width: 760px;
    height: 257px;
    background: var(--card-bg);
    box-shadow: 0 4px 14px rgba(0,0,0,0.28);
    overflow: hidden;
  }
  .banner svg { display: block; width: 100%; height: 100%; }
  .pillar-label {
    font-family: "Montserrat", sans-serif;
    font-weight: 700;
    font-size: 25px;
    fill: var(--label);
  }
  .brand-name {
    font-family: "Montserrat", sans-serif;
    font-weight: 600;
    font-size: 21px;
    letter-spacing: 1px;
    fill: var(--white);
  }
  .method-title {
    font-family: "Montserrat", sans-serif;
    font-weight: 800;
    font-size: 31px;
    fill: var(--white);
  }
  .method-title .accent { fill: var(--orange); }
  .tagline {
    font-family: "Montserrat", sans-serif;
    font-weight: 800;
    font-size: 21px;
    fill: var(--white);
  }
  .headline {
    font-family: "Bebas Neue", sans-serif;
    font-size: 140px;
    fill: var(--white);
  }
  .pillar-icon .ring { fill: var(--orange-ring); }
  .pillar-icon .core { fill: var(--orange); }
  .pillar-icon .glyph { fill: var(--white); }
</style>
</head>
<body>
<main class="stage">
  <section class="banner" aria-label="Keystone Method: seven pillars supporting 85 things">
    <svg viewBox="0 0 1406 476" xmlns="http://www.w3.org/2000/svg">
      <defs>
        <radialGradient id="dome-fill" cx="0.5" cy="0.7" r="0.7">
          <stop offset="0" stop-color="var(--navy-light)"/>
          <stop offset="1" stop-color="var(--navy)"/>
        </radialGradient>
        <radialGradient id="icon-glow">
          <stop offset="0.6" stop-color="var(--orange-glow)" stop-opacity="0.9"/>
          <stop offset="1" stop-color="var(--orange-glow)" stop-opacity="0"/>
        </radialGradient>
        <clipPath id="banner-clip"><rect width="1406" height="476"/></clipPath>
      </defs>

      <g clip-path="url(#banner-clip)">
        <circle cx="703" cy="503" r="428" fill="url(#icon-glow)" opacity="0.5"/>
        <circle class="dome" cx="703" cy="503" r="411" fill="url(#dome-fill)" role="img" aria-label="Navy dome with a faint world map texture"/>
        <circle cx="703" cy="503" r="396" fill="none" stroke="#ffffff" stroke-width="2" stroke-dasharray="2 5" opacity="0.85"/>
      </g>

      <g class="pillar-icon" transform="translate(569 108)">
        <circle r="60" fill="url(#icon-glow)"/><circle class="ring" r="48"/><circle class="core" r="40"/>
        <g class="glyph">
          <rect x="-22" y="-4" width="12" height="24"/><rect x="-6" y="-18" width="12" height="38"/><rect x="10" y="-10" width="12" height="30"/>
        </g>
      </g>
      <g class="pillar-icon" transform="translate(453 172)">
        <circle r="60" fill="url(#icon-glow)"/><circle class="ring" r="48"/><circle class="core" r="40"/>
        <g class="glyph">
          <polygon points="-22,-8 0,-22 22,-8"/><rect x="-20" y="-6" width="40" height="4"/>
          <rect x="-17" y="0" width="5" height="16"/><rect x="-7" y="0" width="5" height="16"/><rect x="3" y="0" width="5" height="16"/><rect x="13" y="0" width="5" height="16"/>
          <rect x="-22" y="17" width="44" height="5"/>
        </g>
      </g>
      <g class="pillar-icon" transform="translate(367 264)">
        <circle r="60" fill="url(#icon-glow)"/><circle class="ring" r="48"/><circle class="core" r="40"/>
        <polygon class="glyph" points="0,-22 24,18 -24,18"/>
        <rect x="-2.5" y="-8" width="5" height="14" fill="var(--orange)"/><rect x="-2.5" y="9" width="5" height="5" fill="var(--orange)"/>
      </g>
      <g class="pillar-icon" transform="translate(307 374)">
        <circle r="60" fill="url(#icon-glow)"/><circle class="ring" r="48"/><circle class="core" r="40"/>
        <g class="glyph">
          <ellipse cx="-2" cy="2" rx="20" ry="14"/><circle cx="18" cy="-2" r="7"/>
          <rect x="-14" y="12" width="6" height="9"/><rect x="4" y="12" width="6" height="9"/>
        </g>
      </g>

      <g class="pillar-icon" transform="translate(837 108)">
        <circle r="60" fill="url(#icon-glow)"/><circle class="ring" r="48"/><circle class="core" r="40"/>
        <g class="glyph">
          <rect x="-22" y="-10" width="44" height="30" rx="3"/>
          <rect x="-8" y="-18" width="16" height="10" rx="2" fill="none" stroke="#fff" stroke-width="4"/>
        </g>
        <rect x="-22" y="2" width="44" height="3" fill="var(--orange)"/>
      </g>
      <g class="pillar-icon" transform="translate(954 172)">
        <circle r="60" fill="url(#icon-glow)"/><circle class="ring" r="48"/><circle class="core" r="40"/>
        <rect class="glyph" x="-22" y="-8" width="44" height="26" rx="2"/>
        <rect x="-17" y="-3" width="34" height="16" fill="none" stroke="var(--orange)" stroke-width="2"/>
        <circle cx="0" cy="5" r="5" fill="var(--orange)"/>
        <polygon class="glyph" points="-16,-12 14,-22 16,-16 -12,-10"/>
      </g>
      <g class="pillar-icon" transform="translate(1039 264)">
        <circle r="60" fill="url(#icon-glow)"/><circle class="ring" r="48"/><circle class="core" r="40"/>
        <path class="glyph" d="M0 20 C-30 0 -24 -20 -10 -20 C-4 -20 0 -15 0 -12 C0 -15 4 -20 10 -20 C24 -20 30 0 0 20 Z"/>
      </g>
      <g class="pillar-icon" transform="translate(1102 374)">
        <circle r="60" fill="url(#icon-glow)"/><circle class="ring" r="48"/><circle class="core" r="40"/>
        <g class="glyph">
          <path d="M-24 -16 h26 v18 h-16 l-8 8 v-8 h-2 z"/>
          <path d="M-4 -6 h28 v20 h-4 v8 l-8 -8 h-16 z" stroke="var(--orange)" stroke-width="2"/>
        </g>
      </g>

      <text class="pillar-label" x="505" y="88" text-anchor="end">Estate Planning</text>
      <text class="pillar-label" x="380" y="171" text-anchor="end">Wealth Management</text>
      <text class="pillar-label" x="293" y="266" text-anchor="end">Risk Management</text>
      <text class="pillar-label" x="238" y="383" text-anchor="end">Tax Planning</text>
      <text class="pillar-label" x="900" y="88">Value Added Services</text>
      <text class="pillar-label" x="1025" y="171">Cash Management</text>
      <text class="pillar-label" x="1110" y="266">Philanthropy</text>
      <text class="pillar-label" x="1172" y="383">The Language</text>

      <circle cx="572" cy="178" r="16" fill="none" stroke="#ffffff" stroke-width="3"/>
      <text class="brand-name" x="598" y="186">TWIN HARBOR CAPITAL</text>

      <text class="method-title" x="703" y="250" text-anchor="middle">KEYSTONE <tspan class="accent">METHOD</tspan></text>
      <rect x="439" y="268" width="528" height="36" fill="var(--band)"/>
      <text class="tagline" x="703" y="294" text-anchor="middle" textLength="496" lengthAdjust="spacingAndGlyphs">OUR PLAN GROWS, AS YOUR LIFE UNFOLDS</text>
      <text class="headline" x="703" y="427" text-anchor="middle" textLength="485" lengthAdjust="spacingAndGlyphs">85 THINGS</text>
    </svg>
  </section>
</main>
</body>
</html>
```